Need simple and modern looking business card with all my information on one side and logo on the other side
Info :
Company name - VELMAR CONSTRUCTION LLC
Company addres- 418 harbor 87th. Dunmoor park ny 10352
Email- velmarllc@tridomail.Com
Company phone number 555-318-6094
Cell number- 555-742-0583
Web site - velmarllc.Com
My name Gerald tomasino

Target Market(s)

Construction , home improvement, remodeling

Industry/Entity Type

Construction

Contact Information for Business Card

It has to be moder but at the same time simple

Font styles to use
Sans Serif

Colors
0255a3
ffffff
000000
f78f20
b1b1b1
9d9d9d
1b1b1b
33a6d7
ec1f27

Requirements
Must have
• My logo on one side maybe with a some kind of background on the other side all my information
Nice to have
• Some kind of background pictures provided by you .PLEASE HAVE ACCOUNT WITH PIXELVAULT WILL NOT PAY ANY EXTRA FEES .
Should not have
• Any kind of hamer, nails,screws, helmets itp. Please do not copy the other designs come up with something new.

```html
<!DOCTYPE html>
<html lang="en">
<head>
<meta charset="utf-8">
<title>Velmar Construction LLC – Business Card</title>
<link href="https://fonts.googleapis.com/css2?family=Open+Sans:wght@400;600;700&display=swap" rel="stylesheet">
<style>
  :root {
    --orange: #f78f20;
    --red: #ec1f27;
    --grey: #9d9d9d;
    --grey-light: #b1b1b1;
    --blue: #0255a3;
    --sky: #33a6d7;
    --ink: #1b1b1b;
    --black: #000000;
    --paper: #ffffff;
    --stage: #e9e9e9;
    --text: #3a3a3a;
  }
  * { box-sizing: border-box; margin: 0; padding: 0; }
  html, body {
    width: 1200px; height: 987px; overflow: hidden;
    background: var(--stage);
    font-family: "Open Sans", Arial, sans-serif;
  }
  .canvas { position: relative; width: 1200px; height: 987px; }

  .card {
    position: absolute; left: 292px; width: 615px; height: 351px;
    overflow: hidden;
  }
  .card--front { top: 130px; background: var(--paper); }
  .card--back { top: 502px; background: var(--ink); }

  /* front */
  .holder-name {
    position: absolute; left: 35px; top: 132px;
    font-size: 19px; font-weight: 700; color: var(--orange); letter-spacing: 0.2px;
  }
  .rule {
    position: absolute; left: 35px; top: 162px; width: 536px; height: 1px;
    background: var(--grey-light);
  }
  .holder-role {
    position: absolute; left: 35px; top: 167px;
    font-size: 14px; font-weight: 600; color: var(--black);
  }
  .brand {
    position: absolute; right: 44px; top: 96px; text-align: right;
    color: var(--ink); font-weight: 700; line-height: 1;
  }
  .brand__main { display: block; font-size: 38px; letter-spacing: 1px; }
  .brand__sub { display: block; font-size: 13.5px; letter-spacing: 1.4px; margin-top: 3px; }

  .contact-list {
    position: absolute; left: 35px; top: 237px; list-style: none;
    font-size: 14.5px; color: var(--text);
  }
  .contact-list li { display: flex; align-items: center; height: 23.5px; }
  .contact-list svg { width: 14px; height: 14px; margin-right: 9px; fill: var(--black); }
  .contact-list .email { font-size: 13.5px; }

  .address {
    position: absolute; right: 44px; top: 237px; text-align: right;
    font-size: 14.5px; color: var(--text); line-height: 23.5px;
  }
  .address .web { font-weight: 700; letter-spacing: 1.2px; color: var(--text); }

  .stripes {
    position: absolute; left: 0; top: 325px; width: 615px; height: 3px;
    display: flex; gap: 4px;
  }
  .stripes span { flex: 1; }
  .stripes .s1 { background: var(--orange); }
  .stripes .s2 { background: var(--red); }
  .stripes .s3 { background: var(--grey); }
  .stripes .s4 { background: var(--blue); }
  .foot-band {
    position: absolute; left: 0; top: 330px; width: 615px; height: 21px;
    background: var(--black);
  }

  /* back */
  .texture {
    position: absolute; inset: 0;
    background: radial-gradient(circle at 50% 45%, #1f1f22 0%, #151517 100%);
  }
  .brand--back {
    position: absolute; left: 0; right: 0; top: 150px; text-align: center;
    color: var(--paper); font-weight: 700; line-height: 1;
  }
  .brand--back .brand__main { font-size: 44px; letter-spacing: 1.5px; }
  .brand--back .brand__sub { font-size: 15.5px; letter-spacing: 1.6px; margin-top: 4px; }
</style>
</head>
<body>
<main class="canvas">

  <section class="card card--front" aria-label="Business card front">
    <div class="brand">
      <span class="brand__main">VELMAR</span>
      <span class="brand__sub">CONSTRUCTION LLC</span>
    </div>

    <p class="holder-name">Gerald tomasino</p>
    <div class="rule"></div>
    <p class="holder-role">CEO/Founder</p>

    <ul class="contact-list">
      <li>
        <svg viewBox="0 0 24 24" aria-hidden="true"><path d="M6.6 10.8a15.1 15.1 0 0 0 6.6 6.6l2.2-2.2c.3-.3.7-.4 1-.2 1.1.4 2.3.6 3.6.6.6 0 1 .4 1 1V20c0 .6-.4 1-1 1A17 17 0 0 1 3 4c0-.6.4-1 1-1h3.5c.6 0 1 .4 1 1 0 1.3.2 2.5.6 3.6.1.3 0 .7-.2 1z"/></svg>
        555-318-6094
      </li>
      <li>
        <svg viewBox="0 0 24 24" aria-hidden="true"><path d="M7 1h10a2 2 0 0 1 2 2v18a2 2 0 0 1-2 2H7a2 2 0 0 1-2-2V3a2 2 0 0 1 2-2zm0 3v14h10V4zm5 15.5a1 1 0 1 0 0 2 1 1 0 0 0 0-2z"/></svg>
        555-742-0583
      </li>
      <li class="email">
        <svg viewBox="0 0 24 24" aria-hidden="true"><path d="M2 5h20v14H2zm2 2v.5l8 5 8-5V7zm0 2.8V17h16V9.8l-8 5z"/></svg>
        velmarllc@tridomail.Com
      </li>
    </ul>

    <address class="address" style="font-style:normal">
      418 harbor 87th.<br>
      Dunmoor park ny 10352<br>
      <span class="web">www.velmarllc.Com</span>
    </address>

    <div class="stripes" aria-hidden="true">
      <span class="s1"></span><span class="s2"></span><span class="s3"></span><span class="s4"></span>
    </div>
    <div class="foot-band"></div>
  </section>

  <section class="card card--back" aria-label="Business card back">
    <div class="texture" role="img" aria-label="Dark textured background with a faint repeating pattern"></div>
    <div class="brand brand--back">
      <span class="brand__main">VELMAR</span>
      <span class="brand__sub">CONSTRUCTION LLC</span>
    </div>
  </section>

</main>
</body>
</html>
```